Redesign of SnapRoute Windows Phone app

The App exists, is up and running but the design is not the best (my creation and i am a developer).
Project landing page http://snaproute.example/

Also the app has live tiles small, medium and large.

The purpose of this is to have a professional design and make this app the best app on the Windows Phone marketplace of his kind.

This app is a picture library that tells you where you've made you're pictures and gives you a unique perspective on the places that you have visited.

If this is successful there will be a version for Windows 8, Android and IOS also.

The app right now is for WP7 and WP8 and because of this the performance is not the best. With this new design the app will be for WP8 only and have the best performance possible.

I am not sure what else should i mention here but i am glad to answer to any questions if you are interested.

I am using Expression design as a design tool and Expression Blend and Visual studio as development tools so if you can provide compatible file the better but is not mandatory.

It wold be nice to keep the existing color palette but again nothing is mandatory I just need a good design.

Links:
App on Marketplace http://www.appmarket.example/en-us/store/app/snaproute/7f3a9d21-8b4c-4e6f-a1d2-93c7b5e08f14

App landing page http://snaproute.example/
Updates

We can do better, I will increase the budget with 200$  so the total budget will be 480$ so please consider this more seriously.

Thank you.

Target Market(s)

Windows Phone users that travel and make pictures.

Industry/Entity Type

Library

Requirements
Must have
• Panorama control as the App main page like in the present.

Representation of visited locations , Live tiles, Map, share location and picture..

If the designer comes up with better proposition they will be take in consideration.

None of these are mandatory but we should keep a connection with the present design so the users will not have the impression that this is a totally different app, this is SnapRoute but better, more professional.

```html
<!DOCTYPE html>
<html lang="en">
<head>
<meta charset="utf-8">
<title>SnapRoute – Panorama</title>
<link rel="stylesheet" href="https://fonts.googleapis.com/css2?family=Roboto+Slab:wght@100;200;300;400&family=Open+Sans:wght@400;600&display=swap">
<style>
  :root{
    --page:#ffffff;
    --blue-deep:#0c4fae;
    --blue-mid:#1f6fd2;
    --blue-glow:#4595ea;
    --blue-dark:#0a3f8f;
    --strip:#5b7396;
    --appbar:#1957ad;
    --toolbar:rgba(120,175,235,0.78);
    --map-land:#ebe6da;
    --map-road:#f5f2ea;
    --tile:rgba(120,180,245,0.35);
    --white:#ffffff;
    --soft:rgba(255,255,255,0.72);
  }
  html,body{margin:0;padding:0;width:1200px;height:807px;overflow:hidden;background:var(--page);}
  .canvas{position:relative;width:1200px;height:807px;overflow:hidden;background:var(--page);}
  .panorama{
    position:absolute;left:52px;top:25px;width:1131px;height:725px;overflow:hidden;
    background:
      radial-gradient(ellipse 420px 300px at 560px 140px, rgba(90,165,245,0.85), transparent 70%),
      radial-gradient(ellipse 260px 220px at 1100px 280px, rgba(8,55,140,0.8), transparent 70%),
      radial-gradient(ellipse 380px 300px at 700px 650px, rgba(80,150,230,0.55), transparent 70%),
      linear-gradient(100deg, var(--blue-deep) 0%, var(--blue-mid) 45%, var(--blue-mid) 70%, var(--blue-deep) 100%);
  }
  .status-strip{position:absolute;left:0;top:0;width:447px;height:24px;background:var(--strip);opacity:.85;}
  .app-title{
    position:absolute;left:42px;top:8px;margin:0;
    font-family:"Roboto Slab",serif;font-weight:200;font-size:138px;line-height:1;
    color:var(--white);letter-spacing:-1px;
  }
  .map-view{position:absolute;left:31px;top:202px;width:350px;height:411px;overflow:hidden;box-shadow:0 2px 8px rgba(0,0,0,.35);}
  .map-area{
    position:absolute;inset:0;
    background:linear-gradient(160deg, var(--map-road) 0%, var(--map-land) 55%, #e2dccd 100%);
  }
  .map-toolbar{position:absolute;left:0;top:0;width:350px;height:73px;background:var(--toolbar);}
  .map-toolbar svg{position:absolute;left:0;top:0;}
  .app-bar{position:absolute;left:0;top:629px;width:447px;height:96px;background:var(--appbar);}
  .app-bar .more{position:absolute;left:402px;top:4px;color:var(--white);font:600 20px/1 "Open Sans",sans-serif;letter-spacing:1px;}
  .bar-button{position:absolute;top:9px;width:90px;text-align:center;}
  .bar-button svg{display:block;margin:0 auto;}
  .bar-button span{display:block;margin-top:6px;color:var(--white);font:400 12px/1 "Roboto Slab",serif;}
  .section-title{
    position:absolute;left:426px;top:196px;margin:0;
    font-family:"Roboto Slab",serif;font-weight:200;font-size:58px;line-height:1;color:var(--white);
  }
  .location{position:absolute;left:457px;}
  .location h3{margin:0;font-family:"Roboto Slab",serif;font-weight:300;font-size:42px;line-height:1;color:var(--white);}
  .location h3 small{font-size:18px;font-weight:300;color:var(--soft);margin-left:4px;}
  .location p{margin:4px 0 0;font:300 13px/1 "Roboto Slab",serif;color:var(--soft);}
  .thumb-grid{position:absolute;left:457px;display:grid;grid-template-columns:repeat(5,49px);grid-auto-rows:49px;gap:6px 7px;}
  .thumb{background:var(--tile);}
</style>
</head>
<body>
<div class="canvas">
  <main class="panorama">
    <div class="status-strip"></div>
    <h1 class="app-title">SnapRoute</h1>

    <section class="map-view">
      <div class="map-area" role="img" aria-label="Street map of the area around the selected location with photo pins"></div>
      <div class="map-toolbar">
        <svg width="350" height="73" viewBox="0 0 350 73" fill="none" stroke="#fff" stroke-width="3" stroke-linecap="round" stroke-linejoin="round">
          <circle cx="37" cy="37" r="19"/><path d="M28 37l6 6 12-12"/>
          <circle cx="92" cy="37" r="19"/><path d="M86 29v12h14"/>
          <circle cx="147" cy="37" r="19"/><path d="M151 28l-9 9 9 9"/>
          <circle cx="203" cy="37" r="19"/><path d="M194 41l9-9 9 9"/>
          <circle cx="258" cy="37" r="19"/><path d="M254 28l9 9-9 9"/>
          <circle cx="311" cy="37" r="19"/><path d="M302 37l6 6 12-12"/>
        </svg>
      </div>
    </section>

    <nav class="app-bar">
      <div class="more">•••</div>
      <div class="bar-button" style="left:107px">
        <svg width="44" height="44" viewBox="0 0 44 44" fill="none" stroke="#fff" stroke-width="3" stroke-linecap="round" stroke-linejoin="round"><circle cx="22" cy="22" r="19"/><path d="M13 22l6 6 12-12"/></svg>
        <span>uncheck</span>
      </div>
      <div class="bar-button" style="left:185px">
        <svg width="44" height="44" viewBox="0 0 44 44" fill="none" stroke="#fff" stroke-width="3" stroke-linecap="round"><circle cx="22" cy="22" r="19"/><path d="M15 15l14 14M29 15L15 29"/></svg>
        <span>clear</span>
      </div>
      <div class="bar-button" style="left:262px">
        <svg width="44" height="44" viewBox="0 0 44 44" fill="none" stroke="#fff" stroke-width="3" stroke-linejoin="round"><circle cx="22" cy="22" r="19"/><path d="M17 13h11v12l-11 7z" fill="#fff"/></svg>
        <span>add to map</span>
      </div>
    </nav>

    <h2 class="section-title">Locations</h2>

    <article class="location" style="top:283px">
      <h3>Lindmoor <small>55pics</small></h3>
      <p>11000,Lindmoor,Estoria</p>
    </article>
    <div class="thumb-grid" style="top:352px">
      <div class="thumb"></div><div class="thumb"></div><div class="thumb"></div><div class="thumb"></div><div class="thumb"></div>
      <div class="thumb"></div><div class="thumb"></div><div class="thumb"></div><div class="thumb"></div><div class="thumb"></div>
    </div>

    <article class="location" style="top:463px">
      <h3>Calderra <small>265pics</small></h3>
      <p>Piazza Aurelia, Calderra</p>
    </article>
    <div class="thumb-grid" style="top:531px">
      <div class="thumb"></div><div class="thumb"></div><div class="thumb"></div><div class="thumb"></div><div class="thumb"></div>
      <div class="thumb"></div><div class="thumb"></div><div class="thumb"></div><div class="thumb"></div><div class="thumb"></div>
    </div>
  </main>
</div>
</body>
</html>
```